Business card for Bright Keystone

Front (space for each) - Name, title, qualifications, mobile number, email address, website, name/logo,
Back - Business name/logo and slogan "your home is our promise" underneath,
in small writing underneath need ABN number, CRN number, ACL number
Target Market(s)
First Home Buyers
Industry/Entity Type
Finance
Contact Information for Business Card
Requirements
Must have
- Front (space for each) - Name, title, qualifications, mobile number, email address, website, name/logo,

```html
<!DOCTYPE html>
<html lang="en">
<head>
<meta charset="UTF-8">
<title>Bright Keystone — Business Card</title>
<link rel="stylesheet" href="https://fonts.googleapis.com/css2?family=Poppins:wght@400;500;600;700&display=swap">
<style>
  :root {
    --bg: #2b2b2d;
    --card-dark: #050505;
    --card-light: #ffffff;
    --ink: #111111;
    --teal: #13a99c;
    --green: #7cc45a;
    --green-soft: #5fbf86;
    --white: #ffffff;
  }
  * { margin: 0; padding: 0; box-sizing: border-box; }
  html, body { width: 1200px; height: 900px; overflow: hidden; }
  body {
    background: var(--bg);
    font-family: "Poppins", sans-serif;
    display: flex;
    flex-direction: column;
    align-items: center;
    justify-content: center;
    gap: 36px;
  }
  .card {
    width: 700px;
    height: 400px;
    border-radius: 26px;
    position: relative;
    overflow: hidden;
    box-shadow: 0 10px 30px rgba(0,0,0,.35);
  }

  /* Back */
  .card--back {
    background: var(--card-dark);
    display: flex;
    flex-direction: column;
    align-items: center;
    justify-content: center;
  }
  .brand__name {
    font-weight: 700;
    font-size: 40px;
    line-height: 1.05;
    letter-spacing: 3px;
    text-transform: uppercase;
  }
  .card--back .brand__name { color: var(--white); }
  .slogan {
    margin-top: 18px;
    color: var(--green);
    font-size: 22px;
    letter-spacing: 1px;
  }
  .registrations {
    position: absolute;
    bottom: 40px;
    left: 0; right: 0;
    text-align: center;
    color: var(--green);
    font-size: 12px;
    letter-spacing: .5px;
    word-spacing: 2px;
  }
  .registrations span { margin: 0 14px; }

  /* Front */
  .card--front {
    background: var(--card-light);
    display: flex;
    align-items: center;
    padding: 0 50px 0 70px;
  }
  .card--front .brand__name { color: var(--ink); font-size: 36px; }
  .divider {
    width: 2px;
    height: 200px;
    background: var(--teal);
    margin: 0 30px 0 40px;
  }
  .person__name {
    font-size: 26px;
    font-weight: 400;
    color: var(--ink);
    line-height: 1.1;
  }
  .person__name strong { font-weight: 700; }
  .person__title {
    color: var(--teal);
    font-size: 17px;
    font-weight: 500;
    margin-top: 4px;
  }
  .person__quals {
    color: var(--green);
    font-size: 17px;
    font-weight: 500;
  }
  .contacts {
    list-style: none;
    margin-top: 14px;
  }
  .contacts li {
    display: flex;
    align-items: center;
    gap: 10px;
    color: var(--ink);
    font-size: 15px;
    margin-top: 8px;
  }
  .contacts svg { width: 22px; height: 22px; flex: none; }
</style>
</head>
<body>

  <section class="card card--back">
    <div class="brand__name">Bright<br>Keystone</div>
    <p class="slogan">your home is our promise</p>
    <p class="registrations">ABN 9876543<span>|</span>CRN 76543210<span>|</span>ACL KS10482</p>
  </section>

  <section class="card card--front">
    <div class="brand__name">Bright<br>Keystone</div>
    <div class="divider"></div>
    <div class="person">
      <h1 class="person__name"><strong>Daniel</strong> Harper</h1>
      <p class="person__title">CEO/Founder</p>
      <p class="person__quals">My qualifications</p>
      <ul class="contacts">
        <li>
          <svg viewBox="0 0 22 22" aria-hidden="true"><circle cx="11" cy="11" r="11" fill="var(--green-soft)"/><rect x="7.5" y="5" width="7" height="12" rx="1.5" fill="none" stroke="#fff" stroke-width="1.4"/><circle cx="11" cy="15" r=".8" fill="#fff"/></svg>
          214-555-0148
        </li>
        <li>
          <svg viewBox="0 0 22 22" aria-hidden="true"><circle cx="11" cy="11" r="11" fill="var(--green-soft)"/><rect x="5.5" y="7" width="11" height="8" rx="1" fill="none" stroke="#fff" stroke-width="1.3"/><path d="M5.5 7.5 11 11.5l5.5-4" fill="none" stroke="#fff" stroke-width="1.3"/></svg>
          daniel@brightkeystone.com
        </li>
        <li>
          <svg viewBox="0 0 22 22" aria-hidden="true"><circle cx="11" cy="11" r="11" fill="var(--green-soft)"/><circle cx="11" cy="11" r="5.5" fill="none" stroke="#fff" stroke-width="1.2"/><ellipse cx="11" cy="11" rx="2.4" ry="5.5" fill="none" stroke="#fff" stroke-width="1.1"/><path d="M5.5 11h11M6.5 8h9M6.5 14h9" stroke="#fff" stroke-width="1"/></svg>
          www.brightkeystone.com
        </li>
      </ul>
    </div>
  </section>

</body>
</html>
```